"Oral Surgery Office needs a Business Card Design with Logo"

We need a logo design and business card. The name of the office is Tassingford Oral Surgery & Implant Center. The final design should communicate uniqueness as well as highly class office. The business card should emphasize power. I included the current business card below. Please design something unique

Target Market(s)

Dentists & Patients

Industry/Entity Type

Dental

Contact Information for Business Card

Unique Design to show success, prestige, Style, unmatched performance

Font styles to use
Serif

Colors
1b1b1b
ffffff
0556a4

Requirements
Must have
• Bussiness Name, Doctor's Name, Website, phone and Fax, email, office address
• Color should be either Black and White or Blue and White
Nice to have
• Clean look
Should not have
• the business card shouldn't be too busy. I feel like the old business card was too busy

```html
<!DOCTYPE html>
<html lang="en">
<head>
<meta charset="utf-8">
<title>Tassingford Oral Surgery &amp; Implant Center — Business Card</title>
<link rel="stylesheet" href="https://fonts.googleapis.com/css2?family=Jost:wght@700&family=Roboto:wght@400;700&family=Roboto+Condensed:wght@400&display=swap">
<style>
  :root {
    --ink: #1b1b1b;
    --paper: #ffffff;
    --brand-blue: #1f62a3;
    --stripe-grey: #9a9a9c;
    --backdrop: #e4e5e7;
  }
  html, body {
    margin: 0;
    padding: 0;
    width: 1200px;
    height: 1200px;
    overflow: hidden;
    background: var(--backdrop);
  }
  .canvas {
    position: relative;
    width: 1200px;
    height: 1200px;
  }
  .card {
    position: absolute;
    left: 220px;
    width: 760px;
    height: 464px;
    display: block;
    box-shadow: 0 14px 26px rgba(0,0,0,0.22);
  }
  .card--front { top: 110px; }
  .card--back { top: 626px; }

  .paper { fill: var(--paper); }
  .corner { fill: var(--ink); }
  .corner-stripe { fill: var(--stripe-grey); }
  .blue-band { fill: var(--brand-blue); }

  .title {
    font-family: "Jost", "Futura", sans-serif;
    font-weight: 700;
    text-anchor: middle;
  }
  .title--city { fill: var(--brand-blue); font-size: 54px; }
  .title--line { fill: var(--ink); font-size: 58px; }
  .title--amp { fill: var(--brand-blue); font-size: 46px; }

  .doctor-name {
    font-family: "Roboto", "Arial", sans-serif;
    font-weight: 700;
    font-size: 36px;
    fill: var(--paper);
    text-anchor: end;
  }
  .doctor-specialty {
    font-family: "Roboto", "Arial", sans-serif;
    font-weight: 400;
    font-size: 23px;
    fill: var(--paper);
    text-anchor: end;
  }

  .contact-text {
    font-family: "Roboto Condensed", "Arial Narrow", sans-serif;
    font-size: 21px;
    fill: var(--paper);
  }
  .contact-text--long { font-size: 19px; }
  .icon-disc { fill: var(--ink); }
  .icon-line { fill: none; stroke: var(--paper); stroke-width: 2.2; stroke-linejoin: round; stroke-linecap: round; }
  .icon-fill { fill: var(--paper); }

  .logo-ring { fill: var(--paper); stroke: var(--brand-blue); stroke-width: 3; }
  .logo-name {
    font-family: "Roboto Condensed", "Arial Narrow", sans-serif;
    font-size: 32px;
    fill: var(--brand-blue);
    text-anchor: middle;
  }
</style>
</head>
<body>
<main class="canvas">

  <!-- Front of card -->
  <svg class="card card--front" viewBox="0 0 898 548" xmlns="http://www.w3.org/2000/svg" aria-label="Business card front">
    <rect class="paper" x="0" y="0" width="898" height="548"/>

    <polygon class="corner-stripe" points="553,0 898,206 898,216 540,0"/>
    <polygon class="corner" points="566,0 898,0 898,206"/>

    <polygon class="corner-stripe" points="0,302 400,548 388,548 0,314"/>
    <polygon class="corner" points="0,314 388,548 0,548"/>

    <text class="title title--city" x="318" y="150">TASSINGFORD</text>
    <text class="title title--line" x="318" y="203">Oral Surgery</text>
    <text class="title title--amp" x="318" y="251">&amp;</text>
    <text class="title title--line" x="318" y="301">Implant Center</text>

    <path class="blue-band" d="M30,345 H528 A75,75 0 0 1 528,495 H30 Z"/>
    <text class="doctor-name" x="560" y="413">Dr. Alden Marrow, D.D.S.</text>
    <text class="doctor-specialty" x="558" y="451">Oral &amp; Maxillofacial Surgery</text>
  </svg>

  <!-- Back of card -->
  <svg class="card card--back" viewBox="0 0 898 548" xmlns="http://www.w3.org/2000/svg" aria-label="Business card back">
    <rect class="paper" x="0" y="0" width="898" height="548"/>

    <polygon class="corner-stripe" points="0,204 336,0 350,0 0,214"/>
    <polygon class="corner" points="0,0 336,0 0,204"/>

    <polygon class="corner-stripe" points="898,302 898,314 522,548 508,548"/>
    <polygon class="corner" points="898,314 898,548 522,548"/>

    <g class="logo">
      <circle class="logo-ring" cx="197" cy="388" r="107"/>
      <text class="logo-name" x="197" y="399">Tassingford</text>
    </g>

    <g class="contact-list">
      <!-- address -->
      <g transform="translate(0,93)">
        <path class="blue-band" d="M432,0 H855 V55 H432 A27.5,27.5 0 0 1 432,0 Z"/>
        <circle class="icon-disc" cx="437" cy="27.5" r="24"/>
        <path class="icon-fill" d="M437,16 L449,28 H445 V38 H440 V31 H434 V38 H429 V28 H425 Z"/>
        <text class="contact-text" x="478" y="35">2740 Harlow Street, Tassingford, NY 11290</text>
      </g>
      <!-- phone -->
      <g transform="translate(0,151)">
        <path class="blue-band" d="M432,0 H855 V55 H432 A27.5,27.5 0 0 1 432,0 Z"/>
        <circle class="icon-disc" cx="437" cy="27.5" r="24"/>
        <path class="icon-fill" d="M425,24 Q437,14 449,24 L447,28 L442,26 V23 Q437,21 432,23 V26 L427,28 Z"/>
        <rect class="icon-fill" x="429" y="29" width="16" height="9" rx="2"/>
        <text class="contact-text" x="478" y="35">555-204-4700</text>
      </g>
      <!-- fax -->
      <g transform="translate(0,209)">
        <path class="blue-band" d="M432,0 H855 V55 H432 A27.5,27.5 0 0 1 432,0 Z"/>
        <circle class="icon-disc" cx="437" cy="27.5" r="24"/>
        <rect class="icon-line" x="427" y="23" width="20" height="14" rx="1"/>
        <path class="icon-line" d="M431,23 V16 H442 L444,18 V23 M430,31 H444"/>
        <text class="contact-text" x="478" y="35">555-204-5006</text>
      </g>
      <!-- email -->
      <g transform="translate(0,266)">
        <path class="blue-band" d="M432,0 H855 V55 H432 A27.5,27.5 0 0 1 432,0 Z"/>
        <circle class="icon-disc" cx="437" cy="27.5" r="24"/>
        <rect class="icon-line" x="427" y="18" width="20" height="16" rx="2"/>
        <path class="icon-line" d="M427,20 L437,28 L447,20"/>
        <text class="contact-text contact-text--long" x="478" y="34">TassingfordOralSurgeon@mailbox.com</text>
      </g>
      <!-- website -->
      <g transform="translate(0,324)">
        <path class="blue-band" d="M432,0 H855 V55 H432 A27.5,27.5 0 0 1 432,0 Z"/>
        <circle class="icon-disc" cx="437" cy="27.5" r="24"/>
        <rect class="icon-line" x="429" y="17" width="16" height="12" rx="1"/>
        <path class="icon-line" d="M425,36 H449 L446,31 H428 Z"/>
        <text class="contact-text contact-text--long" x="478" y="34">www.TassingfordOralSurgeryCenter.com</text>
      </g>
      <!-- social handle -->
      <g transform="translate(0,382)">
        <path class="blue-band" d="M432,0 H855 V55 H432 A27.5,27.5 0 0 1 432,0 Z"/>
        <circle class="icon-disc" cx="437" cy="27.5" r="24"/>
        <circle class="icon-line" cx="437" cy="27.5" r="9"/>
        <text class="contact-text" x="478" y="35">TassingfordOS</text>
      </g>
      <!-- social page -->
      <g transform="translate(0,440)">
        <path class="blue-band" d="M432,0 H855 V55 H432 A27.5,27.5 0 0 1 432,0 Z"/>
        <circle class="icon-disc" cx="437" cy="27.5" r="24"/>
        <rect class="icon-line" x="428" y="18.5" width="18" height="18" rx="2"/>
        <text class="contact-text contact-text--long" x="478" y="34">Tassingford Oral Surgery &amp; Implant Center</text>
      </g>
    </g>
  </svg>

</main>
</body>
</html>
```